Website Design Brief – B2B Industrial Engineering Company

DO NOT CONTACT ME PRIVATELY. ANY INQUIRES WILL BE IGNORED.

1. Industry & Company Background

We are a Swiss B2B engineering and manufacturing company operating in the fields of:
• Industrial air technology (Lufttechnik)
• Metal fabrication and plant construction (Metallbau / Anlagebau)
• Design, fabrication, installation, maintenance, and servicing of:
• Spray booths / paint booths
• Extraction and ventilation systems
• Filtration and environmentally efficient air-handling systems

We plan, build, manufacture, sell, install, and maintain these systems.
Most systems are custom-built in-house (metalwork, apparatus construction, air technology), tailored to customer requirements rather than relying only on standard components.

We are a family-run business with a strong focus on:
• Swiss quality
• Long-term experience
• Reliability and engineering competence
• Environmental efficiency
• Apprenticeship training (we train apprentices in our workshop)

2. Goal of the New Website

The new website should be a modernized evolution of our existing site, not a complete reinvention.

Key objectives:
• Look more modern, fresh, and dynamic
• Clearly communicate our experience, quality, and values
• Emphasize Swiss engineering, tradition, and reliability
• Feel professional and trustworthy, not flashy
• Be clean, uncluttered, and highly structured
• Encourage visitors to submit an inquiry or contact us

The website should feel confident and industrial-premium, with a strong focus on clarity and usability.

3. Overall Design Direction

Visual Style
• Modern industrial design
• Clean layouts with strong structure
• Clear visual hierarchy
• Balanced use of whitespace
• Calm, confident, engineering-focused look

Layout Principles (Important)
• Use clearly separated sections
• Avoid overlapping elements
• Avoid overly complex or experimental layouts
• Prefer grid-based, structured compositions
• Each section should have a clear start and end
• Designs should translate well into standard web layouts without reliance on floating or layered effects

Motion & Media
• A video header on the homepage is strongly desired
• Industrial footage, workshop, fabrication, systems in operation, or environmental technology
• Subtle animations are welcome (e.g., fades, simple transitions)
• Avoid heavy parallax or effects that depend on overlapping elements

4. Target Audience
• Industrial and B2B clients
• Engineers, facility managers, workshop owners
• Decision-makers looking for reliable long-term partners
• Customers who value custom solutions, quality, and service

5. Reference Website

Existing website (content & structure reference):
https://www.kelvorandtech.ch

This site:
• Provides existing branding, colors, and tone
• Is the baseline for content and structure
• Should be visually improved, simplified, and modernized

6. Pages to Design (Initial Phase – 5 Pages)

Please design 5 key pages, based on the existing website structure:
1. Home
• Video header
• Clear value proposition
• Overview of services
• Trust elements (experience, Swiss quality, family business)
• Strong call-to-action (Contact / Request Quote)
2. Company / About Us
• Company history
• Values and philosophy
• Swiss quality and tradition
• Family business
• Apprenticeship training and workshop
3. Services / Solutions
• Planning
• Manufacturing
• Installation
• Maintenance & service
• Custom systems vs standard components
4. Products / Systems
• Spray booths
• Extraction systems
• Filtration and air technology
• Modular but clearly structured sections
5. Contact
• Contact form
• Company details
• Location
• Clear inquiry-focused layout

7. Functional Requirements

Must Have
• Contact form
• Newsletter signup
• Cookie consent (EU / GDPR compliant)
• Privacy policy and legal pages (EU data protection)
• Clear navigation structure
• PDF catalog download area (well organized)

Must NOT Have
• No search feature
• No cluttered mega-menus
• No hidden or confusing navigation

8. Future Expansion (Phase Two – Not Required Now)

Designs should allow future expansion, including:
• Multi-language support (English, French, Italian)
• Optional webshop integration
• Expanded product catalog
• Additional service pages

These features do not need to be designed now, but the layout should be flexible enough to support them later.

9. Colors & Branding
• Use colors similar to the existing website
• Industrial, neutral tones preferred
• Accents should feel technical and professional
• Avoid trendy or overly bright color palettes

10. Tone & Messaging

The design should communicate:
• Experience
• Precision
• Trust
• Environmental responsibility
• Custom engineering capability
• Long-term partnership mindset

The overall impression should be:

“A modern Swiss engineering company with deep experience, strong values, and reliable solutions.”

11. Final Notes for Designers
• Focus on clarity, structure, and usability
• Designs should be realistic to implement with standard web layouts
• Avoid designs that rely on overlapping elements or complex layering
• Think in terms of clean sections, strong grids, and clear content flow
• The primary conversion goal is customer inquiries

Target Market(s)

The target market is B2B industrial customers, not consumers.

Industry/Entity Type

B2B industrial engineering and manufacturing (air technology, metal construction, plant engineering).

Number of Pages Required

5+ page

Requirements
Must have
• Clean structured layout, clear B2B positioning, video header, strong inquiry CTA, contact form, GDPR compliance, PDF downloads.
Nice to have
• Newsletter signup, multilingual-ready structure, future webshop support.
Should not have
• Search feature, overlapping elements, complex layered layouts, cluttered navigation.

```html
<!DOCTYPE html>
<html lang="en">
<head>
<meta charset="utf-8">
<title>Kelvorand – Industrial Solutions</title>
<link href="https://fonts.googleapis.com/css2?family=Archivo:wght@400;500;600;700&display=swap" rel="stylesheet">
<style>
:root{
  --red:#e5261b;
  --ink:#151515;
  --dark:#121212;
  --text:#3c3c3c;
  --muted:#5c5c5c;
  --line:#e2e2e2;
  --soft:#f6f6f6;
  --white:#ffffff;
}
*{box-sizing:border-box;margin:0;padding:0}
html,body{width:1200px;height:3501px;overflow:hidden}
body{font-family:"Archivo",Arial,sans-serif;color:var(--ink);background:var(--white);font-size:11px;line-height:1.5}
.wrap{width:760px;margin:0 auto;position:relative}
a{color:inherit;text-decoration:none}
.red{color:var(--red)}
/* header */
.hero{background:var(--dark);height:222px;color:var(--white)}
.nav{display:flex;align-items:center;justify-content:space-between;height:38px;padding-top:0}
.brand{display:flex;align-items:center;gap:10px;font-weight:700;font-size:12.5px;letter-spacing:.5px}
.brand-mark{width:22px;height:22px;border-radius:5px;background:var(--red)}
.nav-links{display:flex;gap:6px;align-items:center;font-size:11px}
.nav-links a{padding:5px 9px;border-radius:4px}
.nav-links .active{background:#3a3a3a}
.nav-links .cta{background:var(--red);padding:7px 15px;font-weight:600;margin-left:6px}
.hero-body{padding:58px 0 0 120px}
.hero h1{font-size:31px;font-weight:600;letter-spacing:.2px}
.hero p{font-size:11.5px;margin-top:12px;color:#e8e8e8}
/* overview */
.overview{height:342px;padding-top:59px}
.card-row{display:flex;gap:20px}
.card{background:var(--soft);border:1px solid var(--line);border-radius:4px;padding:20px}
.over-card{width:240px;height:224px}
.over-card h3{font-size:15px;font-weight:600}
.over-card p{font-size:10.5px;color:var(--muted);margin-top:8px;line-height:1.55}
.ticks{list-style:none;margin-top:14px}
.ticks li{display:flex;align-items:center;gap:6px;font-size:9px;color:var(--text);margin-bottom:5px}
.ticks svg{flex:none}
.more{display:inline-flex;align-items:center;gap:5px;color:var(--red);font-weight:600;font-size:10px;margin-top:14px}
/* gray products area */
.products{background:var(--soft);height:1638px}
.feature{display:flex;justify-content:space-between;align-items:flex-start}
.feature-text{width:370px}
.eyebrow{color:var(--red);font-size:8.5px;font-weight:600;letter-spacing:1.2px;text-transform:uppercase}
.feature h2{font-size:22px;font-weight:600;margin-top:9px}
.feature .lead{font-size:10px;color:var(--text);margin-top:13px;line-height:1.65}
.checks{list-style:none;margin-top:10px}
.checks li{display:flex;align-items:center;gap:8px;font-size:10px;margin-bottom:8.5px}
.btn{display:inline-block;background:var(--red);color:var(--white);font-weight:600;font-size:10px;padding:8px 20px;border-radius:2px;margin-top:14px}
.media{width:365px;height:239px;border-radius:4px}
.media-booth{background:linear-gradient(135deg,#2e2e2e 0%,#d9dcdf 35%,#f0f2f3 55%,#8a8d90 80%,#2a2a2a 100%)}
.media-duct{background:linear-gradient(160deg,#9aa0a6 0%,#c6cbd0 40%,#6d747b 75%,#2e3338 100%)}
.media-filter{background:linear-gradient(135deg,#e4e9e9 0%,#cfd5d6 50%,#eef1f1 100%)}
.sub-row{display:flex;gap:20px;margin-top:61px}
.sub-card{background:var(--white);border:1px solid var(--line);border-radius:4px;padding:20px}
.sub-card.wide{width:370px;height:193px}
.sub-card h4{font-size:12.5px;font-weight:600}
.sub-card p{font-size:10px;color:var(--text);margin-top:10px;line-height:1.6}
.arrows{list-style:none;margin-top:12px}
.arrows li{font-size:8.5px;color:var(--text);margin-bottom:6px}
.arrows li::before{content:"→";color:var(--red);margin-right:5px}
.sub-card .more{font-size:8.5px;margin-top:10px}
.sub-card.third{width:240px;height:128px}
.divider{height:1px;background:var(--line);margin:60px 0 0}
/* complementary */
.complement{height:458px;padding-top:58px;border-bottom:1px solid var(--line)}
.center-head{text-align:center}
.center-head h2{font-size:22px;font-weight:600}
.center-head p{font-size:10px;color:var(--text);margin-top:8px}
.comp-grid{display:grid;grid-template-columns:repeat(3,240px);gap:22px 20px;margin-top:36px}
.comp-card{height:113px;padding:20px}
.comp-card h4{font-size:11px;font-weight:600}
.comp-card p{font-size:8.5px;color:var(--muted);margin-top:6px;line-height:1.55}
.comp-card .more{font-size:8.5px;margin-top:7px}
/* docs */
.docs{height:368px;padding-top:58px}
.doc-grid{width:519px;margin:34px auto 0;display:grid;grid-template-columns:repeat(2,252px);gap:17px 15px}
.doc{height:44px;border:1px solid var(--line);border-radius:3px;display:flex;align-items:center;justify-content:space-between;padding:0 15px;font-size:9.5px;font-weight:500}
/* cta + footer */
.dark{background:var(--dark);color:var(--white);height:473px;position:relative}
.cta-block{text-align:center;padding-top:60px}
.cta-block h2{font-size:22px;font-weight:600}
.cta-block p{font-size:11px;color:#dcdcdc;margin:12px auto 0;width:420px;line-height:1.6}
.cta-block .btn{margin-top:15px;padding:8px 20px}
.footer{display:grid;grid-template-columns:195px 195px 195px 175px;margin-top:100px}
.footer h5{font-size:10px;font-weight:600;margin-bottom:10px}
.footer li{list-style:none;font-size:8.5px;color:#cfcfcf;margin-bottom:8px;display:flex;align-items:center;gap:6px}
.footer .about{font-size:8.5px;color:#cfcfcf;margin-top:10px;line-height:1.5;width:180px}
.cookie{position:absolute;left:0;right:0;bottom:0;height:68px;background:#0b0b0b;border-top:1px solid #2a2a2a}
.cookie .wrap{display:flex;align-items:center;justify-content:space-between;height:100%;padding-left:20px}
.cookie h6{font-size:10px;font-weight:600}
.cookie p{font-size:8.5px;color:#cfcfcf;margin-top:6px}
.cookie-actions{display:flex;align-items:center;gap:12px}
.btn-outline{border:1px solid #8a8a8a;padding:6px 13px;font-size:9px;border-radius:2px;font-weight:600}
.btn-accept{background:var(--red);padding:7px 16px;font-size:9px;border-radius:2px;font-weight:600}
</style>
</head>
<body>
<svg width="0" height="0" style="position:absolute">
  <defs>
    <symbol id="tick" viewBox="0 0 12 12"><circle cx="6" cy="6" r="5" fill="none" stroke="currentColor" stroke-width="1.1"/><path d="M3.6 6.1l1.6 1.6 3.2-3.3" fill="none" stroke="currentColor" stroke-width="1.1"/></symbol>
    <symbol id="arrow" viewBox="0 0 12 12"><path d="M2 6h8M6.5 2.5L10 6l-3.5 3.5" fill="none" stroke="currentColor" stroke-width="1.3"/></symbol>
    <symbol id="dl" viewBox="0 0 12 12"><path d="M6 1.5v6M3.5 5l2.5 2.5L8.5 5M1.5 8.5v2h9v-2" fill="none" stroke="currentColor" stroke-width="1.1"/></symbol>
  </defs>
</svg>

<header class="hero">
  <div class="wrap">
    <nav class="nav">
      <div class="brand"><span class="brand-mark"></span>KELVORAND</div>
      <div class="nav-links">
        <a>Home</a><a>About</a><a>Services</a><a class="active">Products</a><a class="cta">Contact</a>
      </div>
    </nav>
    <div class="hero-body">
      <h1>Industrial Solutions</h1>
      <p>Custom-engineered systems designed for durability, efficiency, and environmental responsibility.</p>
    </div>
  </div>
</header>

<section class="overview">
  <div class="wrap card-row">
    <article class="card over-card">
      <h3>Spray Booths</h3>
      <p>Modular and custom-built paint and spray systems</p>
      <ul class="ticks">
        <li><svg width="10" height="10"><use href="#tick"/></svg>ECO modular series</li>
        <li><svg width="10" height="10"><use href="#tick"/></svg>SPX professional booths</li>
        <li><svg width="10" height="10"><use href="#tick"/></svg>Custom specifications</li>
        <li><svg width="10" height="10"><use href="#tick"/></svg>LED lighting systems</li>
        <li><svg width="10" height="10"><use href="#tick"/></svg>Heat recovery options</li>
      </ul>
      <a class="more">Learn More <svg width="11" height="11"><use href="#arrow"/></svg></a>
    </article>
    <article class="card over-card">
      <h3>Extraction Systems</h3>
      <p>Efficient color mist and dust removal</p>
      <ul class="ticks">
        <li><svg width="10" height="10"><use href="#tick"/></svg>Farbspritzwand systems</li>
        <li><svg width="10" height="10"><use href="#tick"/></svg>KRS spray stands</li>
        <li><svg width="10" height="10"><use href="#tick"/></svg>Mobile solutions</li>
        <li><svg width="10" height="10"><use href="#tick"/></svg>Wall-mounted options</li>
        <li><svg width="10" height="10"><use href="#tick"/></svg>Adjustable configurations</li>
      </ul>
      <a class="more">Learn More <svg width="11" height="11"><use href="#arrow"/></svg></a>
    </article>
    <article class="card over-card">
      <h3>Air Filtration</h3>
      <p>Advanced filtration and environmental technology</p>
      <ul class="ticks">
        <li><svg width="10" height="10"><use href="#tick"/></svg>High-performance filters</li>
        <li><svg width="10" height="10"><use href="#tick"/></svg>Modular cartridge systems</li>
        <li><svg width="10" height="10"><use href="#tick"/></svg>Replacement programs</li>
        <li><svg width="10" height="10"><use href="#tick"/></svg>Custom ductwork</li>
        <li><svg width="10" height="10"><use href="#tick"/></svg>Environmental compliance</li>
      </ul>
      <a class="more">Learn More <svg width="11" height="11"><use href="#arrow"/></svg></a>
    </article>
  </div>
</section>

<section class="products">
  <div class="wrap" style="padding-top:63px">
    <div class="feature">
      <div class="feature-text">
        <div class="eyebrow">Professional Solutions</div>
        <h2>Spray Booth Systems</h2>
        <p class="lead">Our spray booth systems are engineered for professional painters and industrial operations. Choose from modular ECO series for flexibility or custom SPX systems for specialized requirements.</p>
        <ul class="checks red">
          <li><svg width="11" height="11"><use href="#tick"/></svg><span style="color:var(--ink)">Energy-efficient operation with heat recovery</span></li>
          <li><svg width="11" height="11"><use href="#tick"/></svg><span style="color:var(--ink)">LED lighting for optimal working conditions</span></li>
          <li><svg width="11" height="11"><use href="#tick"/></svg><span style="color:var(--ink)">Adjustable ventilation and air management</span></li>
          <li><svg width="11" height="11"><use href="#tick"/></svg><span style="color:var(--ink)">Durable construction built for heavy use</span></li>
          <li><svg width="11" height="11"><use href="#tick"/></svg><span style="color:var(--ink)">Easy maintenance and filter replacement</span></li>
          <li><svg width="11" height="11"><use href="#tick"/></svg><span style="color:var(--ink)">Environmental compliance and certifications</span></li>
        </ul>
        <a class="btn">Request Specifications</a>
      </div>
      <div class="media media-booth" role="img" aria-label="Photo of a bright white spray booth interior with glass doors" style="margin-top:24px"></div>
    </div>
    <div class="sub-row">
      <article class="sub-card wide">
        <h4>ECO Series</h4>
        <p>Modular, cost-effective booths suitable for various shop sizes and applications.</p>
        <ul class="arrows"><li>Multiple size configurations</li><li>Pre-assembled for quick setup</li><li>Upgradeable components</li></ul>
        <a class="more">Get More Info →</a>
      </article>
      <article class="sub-card wide">
        <h4>SPX Professional</h4>
        <p>Custom-engineered systems for specialized applications and unique facility requirements.</p>
        <ul class="arrows"><li>Fully customizable design</li><li>Advanced controls and monitoring</li><li>Premium materials and finish</li></ul>
        <a class="more">Request Consultation →</a>
      </article>
    </div>
    <div class="divider"></div>

    <div class="feature" style="margin-top:67px">
      <div class="media media-duct" role="img" aria-label="Photo of industrial extraction ducts and fans in a workshop" style="margin-top:23px"></div>
      <div class="feature-text">
        <div class="eyebrow">Color Mist &amp; Dust</div>
        <h2>Extraction &amp; Ventilation</h2>
        <p class="lead">Our extraction systems efficiently remove color mist, overspray, and dust from your work environment. Engineered for flexibility and reliability, they adapt to your workspace layout.</p>
        <ul class="checks red">
          <li><svg width="11" height="11"><use href="#tick"/></svg><span style="color:var(--ink)">Multiple width configurations (0.5m - 5.0m)</span></li>
          <li><svg width="11" height="11"><use href="#tick"/></svg><span style="color:var(--ink)">Mobile and wall-mounted options</span></li>
          <li><svg width="11" height="11"><use href="#tick"/></svg><span style="color:var(--ink)">Integrated filtration systems</span></li>
          <li><svg width="11" height="11"><use href="#tick"/></svg><span style="color:var(--ink)">Low noise operation</span></li>
          <li><svg width="11" height="11"><use href="#tick"/></svg><span style="color:var(--ink)">Simple maintenance and cleaning</span></li>
          <li><svg width="11" height="11"><use href="#tick"/></svg><span style="color:var(--ink)">OSHA and EU compliance</span></li>
        </ul>
        <a class="btn">Get Product Details</a>
      </div>
    </div>
    <div class="sub-row" style="margin-top:30px">
      <article class="sub-card third"><h4>Farbspritzwand</h4><p>Modular spray booth extraction wall systems for professional painters.</p><a class="more">Learn More →</a></article>
      <article class="sub-card third"><h4>KRS Spray Stand</h4><p>Stand-mounted extraction with integrated booth floor and spray platform.</p><a class="more">Learn More →</a></article>
      <article class="sub-card third"><h4>Mobile Solutions</h4><p>Portable extraction units for flexible workshop layouts and job sites.</p><a class="more">Learn More →</a></article>
    </div>
    <div class="divider"></div>

    <div class="feature" style="margin-top:65px">
      <div class="feature-text">
        <div class="eyebrow">Clean Air Solutions</div>
        <h2>Filtration &amp; Air Technology</h2>
        <p class="lead">Advanced filtration systems protect your workspace and the environment. Our multi-stage filters remove particles, odors, and harmful substances while maintaining system efficiency.</p>
        <ul class="checks red">
          <li><svg width="11" height="11"><use href="#tick"/></svg><span style="color:var(--ink)">Multi-stage filtration technology</span></li>
          <li><svg width="11" height="11"><use href="#tick"/></svg><span style="color:var(--ink)">Cartridge and bag filter options</span></li>
          <li><svg width="11" height="11"><use href="#tick"/></svg><span style="color:var(--ink)">Activated carbon odor filters</span></li>
          <li><svg width="11" height="11"><use href="#tick"/></svg><span style="color:var(--ink)">Energy-efficient operation</span></li>
          <li><svg width="11" height="11"><use href="#tick"/></svg><span style="color:var(--ink)">Long filter life reduces replacement costs</span></li>
          <li><svg width="11" height="11"><use href="#tick"/></svg><span style="color:var(--ink)">Environmentally responsible disposal</span></li>
        </ul>
        <a class="btn">Download Catalog</a>
      </div>
      <div class="media media-filter" role="img" aria-label="Illustration of a modular filtration unit with filter cartridges and control cabinet"></div>
    </div>
  </div>
</section>

<section class="complement">
  <div class="wrap">
    <div class="center-head">
      <h2>Complementary Solutions</h2>
      <p>Additional equipment and components for complete system integration</p>
    </div>
    <div class="comp-grid">
      <article class="card comp-card"><h4>LED Cabin Lighting</h4><p>Energy-efficient daylight-quality lighting with 66% energy savings</p><a class="more">Request Info →</a></article>
      <article class="card comp-card"><h4>Paint Drying Table</h4><p>Rotating turntable for even paint application and drying</p><a class="more">Request Info →</a></article>
      <article class="card comp-card"><h4>Rack &amp; Trolley Systems</h4><p>Mobile racks for efficient material handling and storage</p><a class="more">Request Info →</a></article>
      <article class="card comp-card"><h4>Compressor &amp; Air Tools</h4><p>Industrial compressors and accessory equipment for surface prep</p><a class="more">Request Info →</a></article>
      <article class="card comp-card"><h4>Control Systems</h4><p>Advanced electronics and safety controls integrated throughout</p><a class="more">Request Info →</a></article>
      <article class="card comp-card"><h4>Ductwork &amp; Fittings</h4><p>Custom and modular air routing components for any layout</p><a class="more">Request Info →</a></article>
    </div>
  </div>
</section>

<section class="docs">
  <div class="wrap">
    <div class="center-head">
      <h2>Technical Documentation</h2>
      <p>Detailed specs, datasheets, and installation guides available for download</p>
    </div>
    <div class="doc-grid">
      <a class="doc">Complete Product Catalog (PDF)<svg class="red" width="12" height="12"><use href="#dl"/></svg></a>
      <a class="doc">Spray Booth Installation Guide<svg class="red" width="12" height="12"><use href="#dl"/></svg></a>
      <a class="doc">Extraction System Datasheet<svg class="red" width="12" height="12"><use href="#dl"/></svg></a>
      <a class="doc">Filter Replacement Guide<svg class="red" width="12" height="12"><use href="#dl"/></svg></a>
      <a class="doc">Control System Manual<svg class="red" width="12" height="12"><use href="#dl"/></svg></a>
      <a class="doc">Environmental Compliance Information<svg class="red" width="12" height="12"><use href="#dl"/></svg></a>
    </div>
  </div>
</section>

<footer class="dark">
  <div class="cta-block">
    <h2>Need a Custom Solution?</h2>
    <p>Our engineering team can design a system tailored to your exact specifications and facility constraints.</p>
    <a class="btn">Request Custom Quote</a>
  </div>
  <div class="wrap footer">
    <div>
      <div class="brand"><span class="brand-mark"></span>KELVORAND</div>
      <p class="about">Swiss engineering excellence in industrial air technology and custom fabrication since 1967.</p>
    </div>
    <div><h5>Company</h5><ul><li>About Us</li><li>Services</li><li>Products</li><li>Contact</li></ul></div>
    <div><h5>Solutions</h5><ul><li>Spray Booths</li><li>Extraction Systems</li><li>Air Filtration</li><li>Service &amp; Support</li></ul></div>
    <div><h5>Contact</h5><ul>
      <li><svg width="10" height="10" viewBox="0 0 12 12"><path d="M3 1.5l2 2.5-1.2 1.2a6 6 0 003 3L8 7l2.5 2-1 1.5C5 10.5 1.5 7 1.5 2.5z" fill="none" stroke="#cfcfcf" stroke-width="1"/></svg>+41 44 555 01 20</li>
      <li><svg width="10" height="10" viewBox="0 0 12 12"><rect x="1" y="2.5" width="10" height="7" fill="none" stroke="#cfcfcf"/><path d="M1 3l5 3.5L11 3" fill="none" stroke="#cfcfcf"/></svg>info@kelvorandtech.ch</li>
      <li><svg width="10" height="10" viewBox="0 0 12 12"><path d="M6 11s4-4 4-6.5a4 4 0 00-8 0C2 7 6 11 6 11z" fill="none" stroke="#cfcfcf"/><circle cx="6" cy="4.5" r="1.3" fill="none" stroke="#cfcfcf"/></svg>Switzerland</li>
    </ul></div>
  </div>
  <div class="cookie">
    <div class="wrap">
      <div>
        <h6>Cookie Consent</h6>
        <p>We use cookies to enhance your experience and analyze site traffic. By continuing to use this site, you agree to our use of cookies. <span class="red">Learn more</span></p>
      </div>
      <div class="cookie-actions">
        <a class="btn-outline">Reject</a>
        <a class="btn-accept">Accept</a>
        <svg width="10" height="10" viewBox="0 0 10 10"><path d="M1 1l8 8M9 1L1 9" stroke="#cfcfcf" stroke-width="1.2"/></svg>
      </div>
    </div>
  </div>
</footer>
</body>
</html>
```